Business Card Velostra - Accounting firm

Hi my friend.
I'm coming back to you to see if it would be possible for you to make a modern and minimalist business card design.
In shades of blue like the great logo you offered me.
The ideal is a modern and aesthetic business card.
The goal is to give a professional effect to the first exchanges.
Renewal and innovation in the accounting world !!
I thank you !!
Good evening to you

Target Market(s)

Young, dynamic and sensitive to marketing

Industry/Entity Type

Finance And Accounting

Contact Information for Business Card

Company logo and name. Last name, First name, Phone number, email address, company address, website.

Font styles to use
Sans Serif

Requirements
Must have
• The ideal is a modern and aesthetic business card.

Mentions to include: Company logo and name. Last name, First name, Phone number, email address, company address, website.
Nice to have
• The goal is to give a professional effect to the first exchanges.
Should not have
• Simplistic or childish design

```html
<!DOCTYPE html>
<html lang="en">
<head>
<meta charset="utf-8">
<title>Velostra – Business Card</title>
<link href="https://fonts.googleapis.com/css2?family=Arimo:wght@400;700&display=swap" rel="stylesheet">
<style>
  :root {
    --navy: #0b2a78;
    --navy-deep: #062063;
    --navy-mid: #0d3694;
    --teal: #3fd3c0;
    --blue: #1a8ed6;
    --ink: #111a2b;
    --link: #1f3fa8;
    --paper: #ffffff;
    --rule: #c9ced8;
    --backdrop: #2b2d31;
  }
  * { box-sizing: border-box; margin: 0; padding: 0; }
  html, body {
    width: 1200px; height: 1015px; overflow: hidden;
    background: var(--backdrop);
    font-family: "Arimo", Arial, sans-serif;
  }
  .stage {
    width: 1200px; height: 1015px;
    display: flex; flex-direction: column; align-items: center; justify-content: center;
    gap: 48px;
  }
  .card {
    width: 780px; height: 446px;
    position: relative; overflow: hidden;
    box-shadow: 0 18px 40px rgba(0,0,0,.45);
  }

  /* Front */
  .card--front { background: var(--navy); }
  .front-pattern {
    position: absolute; inset: 0;
    background: linear-gradient(135deg, var(--navy-mid) 0%, var(--navy) 50%, var(--navy-deep) 100%);
  }
  .front-brand {
    position: absolute; right: 120px; bottom: 120px;
    display: flex; align-items: center; gap: 22px;
  }
  .front-brand .brand-mark {
    width: 40px; height: 40px; background: var(--teal);
  }
  .front-brand .brand-name {
    font-weight: 700; font-size: 74px; color: var(--paper); letter-spacing: -1px;
  }

  /* Back */
  .card--back { background: var(--paper); display: flex; }
  .back-brand {
    width: 390px; display: flex; flex-direction: column; align-items: center; justify-content: center;
  }
  .back-brand .brand-mark {
    width: 120px; height: 120px; border-radius: 50%;
    background: linear-gradient(135deg, var(--teal), var(--blue));
    margin-bottom: 26px;
  }
  .back-brand .brand-name {
    font-weight: 700; font-size: 66px; color: var(--navy); letter-spacing: -1px; line-height: 1;
  }
  .back-brand .brand-tagline {
    margin-top: 8px; font-size: 13px; letter-spacing: 7px; color: var(--navy); font-weight: 700;
  }
  .divider {
    width: 1px; background: var(--rule); margin: 80px 0 90px;
  }
  .contact {
    flex: 1; padding: 92px 0 0 38px; color: var(--ink);
  }
  .contact .person-name {
    font-weight: 700; font-size: 28px; color: var(--navy); letter-spacing: .3px;
  }
  .contact .person-role { font-size: 20px; margin-top: 2px; }
  .contact-list { list-style: none; margin-top: 24px; }
  .contact-list li {
    display: flex; align-items: center; gap: 12px; font-size: 20px; line-height: 30px;
  }
  .contact-list svg { width: 20px; height: 20px; fill: var(--navy); flex: none; }
  .contact-list .web-name { color: var(--link); }
  .address { margin-top: 22px; font-size: 20px; line-height: 26px; padding-left: 32px; }
</style>
</head>
<body>
<main class="stage">
  <section class="card card--front">
    <div class="front-pattern" role="img" aria-label="Repeating pattern of the brand symbol in tonal navy blues"></div>
    <div class="front-brand">
      <span class="brand-mark"></span>
      <span class="brand-name">velostra</span>
    </div>
  </section>

  <section class="card card--back">
    <div class="back-brand">
      <span class="brand-mark"></span>
      <span class="brand-name">velostra</span>
      <span class="brand-tagline">EXPERT-COMPTABLE</span>
    </div>
    <div class="divider"></div>
    <div class="contact">
      <p class="person-name">MARCUS DELANEY</p>
      <p class="person-role">Managing Director</p>
      <ul class="contact-list">
        <li>
          <svg viewBox="0 0 24 24" aria-hidden="true"><path d="M6.6 10.8a15.1 15.1 0 0 0 6.6 6.6l2.2-2.2a1 1 0 0 1 1-.25 11.4 11.4 0 0 0 3.6.57 1 1 0 0 1 1 1V20a1 1 0 0 1-1 1A17 17 0 0 1 3 4a1 1 0 0 1 1-1h3.5a1 1 0 0 1 1 1c0 1.25.2 2.45.57 3.57a1 1 0 0 1-.25 1z"/></svg>
          044-870 215 364
        </li>
        <li>
          <svg viewBox="0 0 24 24" aria-hidden="true"><path d="M2 5h20v14H2zm2 2v.5l8 5 8-5V7zm0 3v7h16v-7l-8 5z"/></svg>
          info@velostra.com
        </li>
        <li>
          <svg viewBox="0 0 24 24" aria-hidden="true"><path d="M12 2a10 10 0 1 0 0 20 10 10 0 0 0 0-20zm6.9 6h-3a15 15 0 0 0-1.3-4A8 8 0 0 1 18.9 8zM12 4c.8 1.1 1.5 2.5 1.9 4h-3.8c.4-1.5 1.1-2.9 1.9-4zM4.3 14a8 8 0 0 1 0-4h3.4a16 16 0 0 0 0 4zm.8 2h3a15 15 0 0 0 1.3 4A8 8 0 0 1 5.1 16zm3-8h-3a8 8 0 0 1 4.3-4 15 15 0 0 0-1.3 4zM12 20c-.8-1.1-1.5-2.5-1.9-4h3.8c-.4 1.5-1.1 2.9-1.9 4zm2.3-6H9.7a14 14 0 0 1 0-4h4.6a14 14 0 0 1 0 4zm.3 6a15 15 0 0 0 1.3-4h3a8 8 0 0 1-4.3 4zm1.7-6a16 16 0 0 0 0-4h3.4a8 8 0 0 1 0 4z"/></svg>
          <span>www.<span class="web-name">velostra</span>.com</span>
        </li>
      </ul>
      <p class="address">18 Rue Delmont, Lyon<br>France, 69002</p>
    </div>
  </section>
</main>
</body>
</html>
```